IT Company requires design for Vinyl Print for Glazing NEW FITOUT!

Provide a design for Vinyl Glazing for 7 x 3.5 Metre Loading Bay - Was a warehouse - Conversion to corporate Office - the job is just for a design for the 7 x 3.5 metre loading bay area that will be glazed. We will be covering the Glaze with printed vinyl and we need a design for that. REFER TO GLASS FRONT SIGNAGE MOCK UP in image please.

We are a service and strategy focused IT Services business - 100% outsourced IT for our clients.

Something with more impact than the attached document - See Glass Front Signage page for the requirement.

Please feel free to give me a call

0438 215 906

Regards

Colin
Updates

HI - thanks for taking a look at the project Please see glass front signage in PDF for the best way to help us. Thanks Colin

I have just uploaded the mockups and roller door where the glazing goes in images.

Hi Everyone how is this going?? What do you need from me to assist with getting some designs??

Colin

Target Market(s)

business wanting the very best in IT advice and support

Industry/Entity Type

Business

Font styles to use
Other font styles liked:
• NeoSansPro

Requirements
Must have
• - Simple but with impact
Should not have
• too many colours or photos

```html
<!DOCTYPE html>
<html lang="en">
<head>
<meta charset="utf-8">
<title>Harbourline Systems – Glazing Vinyl</title>
<link rel="stylesheet" href="https://fonts.googleapis.com/css2?family=Encode+Sans:wght@700;800&display=swap">
<style>
  :root {
    --navy: #023a5c;
    --green: #62bb5f;
    --white: #ffffff;
    --frame: #9a9a9a;
  }
  * { margin: 0; padding: 0; box-sizing: border-box; }
  html, body {
    width: 1200px;
    height: 601px;
    overflow: hidden;
    background: var(--white);
  }
  .vinyl {
    position: relative;
    width: 1200px;
    height: 601px;
    border: 1px solid var(--frame);
    background: var(--white);
    font-family: "Encode Sans", "Helvetica Neue", Arial, sans-serif;
  }
  .brand {
    position: absolute;
    left: 228px;
    top: 45px;
    display: flex;
    align-items: center;
    gap: 34px;
  }
  .brand-square {
    width: 190px;
    height: 215px;
    background: var(--green);
    flex: none;
  }
  .brand-name {
    color: var(--navy);
    font-weight: 800;
    line-height: 0.95;
  }
  .brand-name .word-main {
    display: block;
    font-size: 104px;
    letter-spacing: -2px;
  }
  .brand-name .word-sub {
    display: block;
    font-size: 52px;
    letter-spacing: 12px;
    margin-top: 14px;
  }
  .contact-band {
    position: absolute;
    left: 0;
    right: 0;
    top: 313px;
    bottom: 0;
    background: var(--navy);
    text-align: center;
  }
  .invite {
    margin-top: 44px;
    color: var(--green);
    font-weight: 800;
    font-size: 49px;
    letter-spacing: 0.5px;
  }
  .phone {
    margin-top: 6px;
    color: var(--white);
    font-weight: 800;
    font-size: 122px;
    letter-spacing: 3px;
    line-height: 1.1;
  }
</style>
</head>
<body>
  <main class="vinyl">
    <header class="brand">
      <div class="brand-square" aria-hidden="true"></div>
      <h1 class="brand-name">
        <span class="word-main">harbourline</span>
        <span class="word-sub">SYSTEMS</span>
      </h1>
    </header>
    <section class="contact-band">
      <p class="invite">Please feel free to give me a call</p>
      <p class="phone">0438 215 906</p>
    </section>
  </main>
</body>
</html>
```